Vondrake - Waste to Fuel Power Needs A Website

Make website explaining the concept and the team behind the company
Updates

I will be providing A logo and Information about the company upon signed NDA.

Coding

Coded - Design and coding required

Number of Pages Required

5+ page

```html
<!DOCTYPE html>
<html lang="en">
<head>
<meta charset="utf-8">
<title>Vondrake - Waste to Fuel Power</title>
<link href="https://fonts.googleapis.com/css2?family=Oswald:wght@500;600;700&family=Open+Sans:wght@400;600;700&display=swap" rel="stylesheet">
<style>
:root{
  --orange:#f28c13;
  --black:#0b0b0b;
  --white:#ffffff;
  --ink:#141414;
  --text:#3a3a3a;
  --grey:#ececec;
  --field:#1c1c1c;
}
*{box-sizing:border-box;margin:0;padding:0}
html,body{width:1200px;height:4992px;overflow:hidden}
body{position:relative;background:var(--white);font-family:'Open Sans',Arial,sans-serif;color:var(--text)}
.abs{position:absolute}
.head{font-family:'Oswald',Arial,sans-serif;text-transform:uppercase;color:var(--ink);font-weight:600;letter-spacing:.5px}
.btn{position:absolute;background:var(--orange);color:var(--white);font-family:'Oswald',Arial,sans-serif;font-size:14px;font-weight:600;text-transform:uppercase;display:flex;align-items:center;justify-content:center;letter-spacing:.5px}
.photo{position:absolute}
p.body{font-size:15px;line-height:22px}

/* hero */
.hero{left:0;top:0;width:1200px;height:622px;background:linear-gradient(100deg,#e9ecef 0%,#c7ccd1 40%,#6c7075 70%,#2a2c2f 100%)}
.topbar{left:0;top:0;width:1200px;height:100px;background:linear-gradient(#1a1a1a,rgba(26,26,26,.0))}
.brand{font-family:'Oswald',Arial,sans-serif;font-weight:700;font-size:40px;color:var(--white);letter-spacing:1px}
.nav{left:303px;top:38px;display:flex;gap:40px;font-family:'Oswald',Arial,sans-serif;font-size:15px;color:var(--white);font-weight:600;text-transform:uppercase}
.hero-title{left:92px;top:356px;font-size:46px;line-height:54px;color:#1b1e3a;font-weight:700}

/* tech */
.tech-col{width:280px}
.tech-col h3{font-family:'Open Sans',Arial,sans-serif;color:var(--orange);font-size:19px;line-height:23px;font-weight:700;margin-bottom:12px}
.rule{position:absolute;height:4px;background:var(--orange)}

/* about */
.about h2{color:var(--white)}
.about-sub{font-family:'Oswald',Arial,sans-serif;color:var(--orange);font-size:20px;line-height:26px;font-weight:600;text-transform:uppercase}

.cap{font-family:'Oswald',Arial,sans-serif;color:var(--ink);font-size:24px;line-height:30px;font-weight:600;text-transform:uppercase}
.field{position:absolute;border:1px solid #5a5a5a;background:var(--field);color:#cfcfcf;font-size:13px;padding:8px 10px}
.foot-h{font-family:'Oswald',Arial,sans-serif;font-weight:600;font-size:20px;color:#1b1e3a;text-transform:uppercase}
.foot-list{font-size:17px;line-height:27px;color:#333;list-style:none}
</style>
</head>
<body>

<!-- Hero -->
<div class="photo abs hero" role="img" aria-label="Close-up of fuel pump nozzles at a diesel station"></div>
<div class="abs topbar"></div>
<div class="abs brand" style="left:98px;top:22px">VONDRAKE</div>
<nav class="abs nav"><span>About us</span><span>Technology</span><span>What we do</span><span>Sustainability</span><span>Process</span><span>Contact</span></nav>
<div class="btn" style="left:992px;top:30px;width:124px;height:34px;clip-path:polygon(8% 0,100% 0,92% 100%,0 100%)">Get a quote</div>
<h1 class="abs head hero-title">Vondrake is plastic<br>to diesel energy</h1>
<div class="btn" style="left:92px;top:472px;width:116px;height:34px">Get a quote</div>

<!-- Technology -->
<h2 class="abs head" style="left:120px;top:712px;font-size:44px">Our technology &amp; process</h2>
<div class="rule" style="left:120px;top:776px;width:300px"></div>
<svg class="abs" style="left:120px;top:850px" width="90" height="90" viewBox="0 0 90 90" fill="none" stroke="#f28c13" stroke-width="3"><path d="M8 82V40l20 12V40l20 12V40l20 12V20h12v62z"/><rect x="20" y="62" width="10" height="10"/><rect x="44" y="62" width="10" height="10"/><path d="M70 14c4-6 10-6 12-10"/></svg>
<svg class="abs" style="left:470px;top:850px" width="90" height="90" viewBox="0 0 90 90" fill="none" stroke="#f28c13" stroke-width="3"><path d="M30 20l15-12 15 12"/><path d="M68 34l8 20-14 14"/><path d="M52 82H28L14 62l8-18"/><path d="M36 46c8-10 20-8 22 2-4 10-16 12-22 6z"/></svg>
<svg class="abs" style="left:820px;top:850px" width="90" height="90" viewBox="0 0 90 90" fill="none" stroke="#f28c13" stroke-width="3"><rect x="14" y="10" width="40" height="72" rx="3"/><rect x="22" y="18" width="24" height="18"/><path d="M54 30h10l8 10v32a5 5 0 0 1-10 0V52h-8"/><path d="M8 82h52"/></svg>
<div class="abs tech-col" style="left:120px;top:970px"><h3>Lorem ipsum dolor sit ameconsect etur</h3><p class="body">Lorem ipsum dolor sit amet, conse ctetur adipiscing elit, sed do eius mo tempor incididunt ut labore et dolore magna aliqua.</p></div>
<div class="abs tech-col" style="left:470px;top:970px"><h3>Lorem ipsum dolor sit ameconsect etur</h3><p class="body">Lorem ipsum dolor sit amet, conse ctetur adipiscing elit, sed do eius mo tempor incididunt ut labore et dolore magna aliqua.</p></div>
<div class="abs tech-col" style="left:820px;top:970px"><h3>Lorem ipsum dolor sit ameconsect etur</h3><p class="body">Lorem ipsum dolor sit amet, conse ctetur adipiscing elit, sed do eius mo tempor incididunt ut labore et dolore magna aliqua.</p></div>

<!-- About -->
<svg class="abs" style="left:0;top:1180px" width="1200" height="800" viewBox="0 0 1200 800"><polygon points="0,120 1200,0 1200,710 0,780" fill="#0b0b0b"/></svg>
<section class="about">
<h2 class="abs head" style="left:120px;top:1384px;font-size:40px;color:var(--white)">About us</h2>
<div class="rule" style="left:120px;top:1440px;width:170px"></div>
<div class="abs about-sub" style="left:120px;top:1462px;width:420px">Lorem ipsum dolor sit amet conse cteteur adipiscing elitsed do</div>
<p class="abs body" style="left:120px;top:1532px;width:420px;color:#d8d8d8">Lorem ipsum dolor sit amet, consectetur adipiscing elit, sed do eiusmod tempor incididunt ut labore et dolore magna aliqua. Quis ipsum suspendisse ultrices gravida. Risus commodo viverra maecenas accumsan lacus vel facilisis sed dolor sit amet, consectetur adipiscing elit, sed do eiusmod tempor incididunt ut labore et dolore magna aliqua.</p>
<div class="btn" style="left:120px;top:1706px;width:112px;height:34px">Get a quote</div>
<div class="abs" style="left:652px;top:1358px;width:392px;height:556px;border:5px solid var(--orange)"></div>
<div class="photo" style="left:612px;top:1372px;width:420px;height:546px;background:linear-gradient(150deg,#6d5d48,#3a3229 55%,#1c1915)" role="img" aria-label="Two engineers in caps working on industrial machinery"></div>
</section>

<!-- Proven technology -->
<h2 class="abs head" style="left:0;top:2012px;width:1200px;text-align:center;font-size:44px;line-height:54px">The proven recycling<br>technology for plastics</h2>
<div class="photo" style="left:120px;top:2156px;width:480px;height:310px;background:linear-gradient(170deg,#9fc6e4,#d9d2c0 50%,#b57a3f)" role="img" aria-label="Refinery towers against a sunlit sky"></div>
<div class="photo" style="left:650px;top:2156px;width:480px;height:310px;background:linear-gradient(160deg,#a8acae,#dfe2e2 50%,#6b8a74)" role="img" aria-label="Worker sorting bags of plastic waste in a recycling plant"></div>
<div class="abs cap" style="left:120px;top:2490px;width:480px">Lorem ipsum dolor sit amet consecte tur adipiscing elit &nbsp;sed loremdo</div>
<p class="abs body" style="left:120px;top:2560px;width:470px">Lorem ipsum dolor sit amet, consectetur adipiscing elit, sed do eiusmod tempor incididunt ut labore et dolore magna aliqua. Quis ipsum suspendisse ultrices gravida. Risus commodo viverra maecenas accumsan.</p>
<div class="abs cap" style="left:650px;top:2490px;width:480px">Lorem ipsum dolor sit amet consecte tur adipiscing elit &nbsp;sed loremdo</div>
<p class="abs body" style="left:650px;top:2560px;width:470px">Lorem ipsum dolor sit amet, consectetur adipiscing elit, sed do eiusmod tempor incididunt ut labore et dolore magna aliqua. Quis ipsum suspendisse ultrices gravida. Risus commodo viverra maecenas accumsan.</p>

<!-- Mission band -->
<svg class="abs" style="left:0;top:2752px" width="1200" height="560" viewBox="0 0 1200 560"><polygon points="0,0 600,0 600,72 1200,72 1200,560 0,560" fill="#f28c13"/></svg>
<h2 class="abs head" style="left:122px;top:2858px;font-size:42px;line-height:52px;color:var(--white)">Cleaning the planet.<br>Fueling the future.</h2>
<p class="abs body" style="left:612px;top:2826px;width:470px;color:var(--white)">Lorem ipsum dolor sit amet, consectetur adipiscing elit, sed do eiusmod tempor incididunt ut labore et dolore magna aliqua. Quis ipsum suspendisse ultrices gravida. Risus commodo viverra maecenas accumsan lacus vel facilisis.</p>
<p class="abs body" style="left:612px;top:2956px;width:470px;color:var(--white)">Lorem ipsum dolor sit amet, consectetur adipiscing elit, sed do eiusmod tempor incididunt ut labore et dolore magna aliqua. Quis ipsum suspendisse ultrices gravida. Risus commodo viverra maecenas accumsan lacus vel facilisis.</p>
<div class="photo" style="left:56px;top:3132px;width:510px;height:214px;background:linear-gradient(160deg,#f0c07a,#9a8c86 45%,#3f4a55)" role="img" aria-label="Industrial pipework and tanks at sunset"></div>

<!-- What we do -->
<h2 class="abs head" style="left:0;top:3460px;width:1200px;text-align:center;font-size:44px">What we do</h2>
<div class="photo" style="left:120px;top:3540px;width:280px;height:282px;background:linear-gradient(150deg,#b9d3e6,#3d7fb5 55%,#d2a36c)" role="img" aria-label="Gloved hand collecting plastic bottles"></div>
<div class="photo" style="left:450px;top:3540px;width:300px;height:282px;background:radial-gradient(circle at 50% 45%,#d6ecc0,#5b9b3c 55%,#2a5a20)" role="img" aria-label="Hands holding a glass globe over green foliage"></div>
<div class="photo" style="left:790px;top:3540px;width:290px;height:282px;background:linear-gradient(150deg,#e6eef4,#8fb5d4 50%,#f1cd46)" role="img" aria-label="Laboratory flasks of fuel samples"></div>
<div class="abs cap" style="left:120px;top:3846px;width:280px;font-size:22px;line-height:28px">Lorem ipsum dolor sit ame consect</div>
<p class="abs body" style="left:120px;top:3914px;width:280px;font-size:14px;line-height:20px">Lorem ipsum dolor sit amet, conse ctetur adipiscing elit, sed do eius mo tempor incididunt ut labore et dolore magna aliqua. Quis ipsum suspen disse ultrices gravida.</p>
<div class="abs cap" style="left:450px;top:3846px;width:290px;font-size:22px;line-height:28px">Lorem ipsum dolor sit ame consect</div>
<p class="abs body" style="left:450px;top:3914px;width:290px;font-size:14px;line-height:20px">Lorem ipsum dolor sit amet, conse ctetur adipiscing elit, sed do eius mo tempor incididunt ut labore et dolore magna aliqua. Quis ipsum suspen disse ultrices gravida.</p>
<div class="abs cap" style="left:790px;top:3846px;width:290px;font-size:22px;line-height:28px">Lorem ipsum dolor sit ame consect</div>
<p class="abs body" style="left:790px;top:3914px;width:290px;font-size:14px;line-height:20px">Lorem ipsum dolor sit amet, conse ctetur adipiscing elit, sed do eius mo tempor incididunt ut labore et dolore magna aliqua. Quis ipsum suspen disse ultrices gravida.</p>

<!-- Contact -->
<svg class="abs" style="left:0;top:4098px" width="1200" height="400" viewBox="0 0 1200 400"><polygon points="0,0 1200,0 1200,300 0,394" fill="#0b0b0b"/></svg>
<h2 class="abs head" style="left:120px;top:4228px;font-size:42px;color:var(--white)">Contact us</h2>
<div class="rule" style="left:120px;top:4284px;width:150px"></div>
<p class="abs body" style="left:120px;top:4304px;width:300px;color:var(--white);font-size:17px;line-height:22px">Lorem ipsum dolor sit ametconsectetur adipiscing elit &nbsp;sed do eiusmod tem.</p>
<div class="field" style="left:512px;top:4216px;width:250px;height:44px">Name</div>
<div class="field" style="left:776px;top:4216px;width:250px;height:44px">Email</div>
<div class="field" style="left:512px;top:4276px;width:250px;height:44px">Phone</div>
<div class="field" style="left:776px;top:4276px;width:250px;height:44px">Subject</div>
<div class="field" style="left:512px;top:4336px;width:514px;height:86px">Message</div>
<div class="btn" style="left:904px;top:4436px;width:122px;height:38px">Submit</div>

<!-- Footer -->
<footer>
<div class="abs" style="left:0;top:4492px;width:1200px;height:500px;background:linear-gradient(180deg,#ffffff 0%,#e7e7e7 100%);clip-path:polygon(0 0,1200px 0,1200px 100%,0 100%)"></div>
<svg class="abs" style="left:0;top:4398px" width="1200" height="100" viewBox="0 0 1200 100"><polygon points="0,94 1200,0 1200,100 0,100" fill="#f7f7f7"/></svg>
<div class="abs" style="left:120px;top:4596px;font-family:'Oswald',Arial,sans-serif;font-weight:700;font-size:62px;color:var(--ink);letter-spacing:1px">VONDRAKE</div>
<div class="abs" style="left:422px;top:4536px;width:1px;height:294px;background:#c9c9c9"></div>
<div class="abs" style="left:780px;top:4536px;width:1px;height:294px;background:#c9c9c9"></div>
<div class="abs foot-h" style="left:534px;top:4538px">Links</div>
<div class="rule" style="left:534px;top:4572px;width:40px;height:3px"></div>
<ul class="abs foot-list" style="left:534px;top:4584px"><li>Home</li><li>About Us</li><li>Process</li><li>Services</li><li>Contact</li></ul>
<div class="abs foot-h" style="left:840px;top:4538px">Contact</div>
<div class="rule" style="left:840px;top:4572px;width:40px;height:3px"></div>
<ul class="abs foot-list" style="left:840px;top:4588px;line-height:34px">
<li><svg width="18" height="18" viewBox="0 0 24 24" style="vertical-align:-3px;margin-right:10px"><path fill="#f28c13" d="M6.6 10.8a15.1 15.1 0 0 0 6.6 6.6l2.2-2.2c.3-.3.7-.4 1-.2 1.1.4 2.3.6 3.6.6.6 0 1 .4 1 1V20c0 .6-.4 1-1 1A17 17 0 0 1 3 4c0-.6.4-1 1-1h3.5c.6 0 1 .4 1 1 0 1.3.2 2.5.6 3.6.1.3 0 .7-.2 1z"/></svg>0491 570 156</li>
<li><svg width="18" height="18" viewBox="0 0 24 24" style="vertical-align:-3px;margin-right:10px"><rect x="2" y="5" width="20" height="14" rx="2" fill="#f28c13"/><path d="M3 6l9 7 9-7" fill="none" stroke="#fff" stroke-width="1.6"/></svg>info@vondrake.com.au</li>
<li><svg width="18" height="18" viewBox="0 0 24 24" style="vertical-align:-3px;margin-right:10px"><path fill="#f28c13" d="M12 2a7 7 0 0 0-7 7c0 5 7 13 7 13s7-8 7-13a7 7 0 0 0-7-7zm0 9.5A2.5 2.5 0 1 1 12 6.5a2.5 2.5 0 0 1 0 5z"/></svg>Location: Australia</li>
</ul>
<div class="abs" style="left:120px;top:4872px;width:960px;height:1px;background:#c9c9c9"></div>
<div class="abs" style="left:0;top:4900px;width:1200px;text-align:center;font-size:14px;color:#555">Copyright 2025. All Rights are Reserved. Privacy Policy</div>
</footer>

</body>
</html>
```